Plumbing Trifold Design for Restoration Company

We would like this brochure to match our current KVT branding and marketing materials. The overall look should feel modern, clean, premium, and trustworthy.

Our brand colors are included in the attached files along with a picture of what our current marketing material looks like. We'd like to use real KVT photography whenever possible rather than stock images, but if stock images are necessary, please go ahead and use.

The brochure should communicate that KVT is a full-service plumbing company backed by years of experience in both traditional plumbing and complex pipe restoration.

Front Page: we would like to include logo, phone number (800-318-4957), website (www.kvtflow.example) and then maybe the following: "Traditional Plumbing Services", "residential & commercial, 24/7 Emergency Service, Licensed & Insured" and can also add "reliable Repairs. Honest Service. Lasting Solutions" if spacing allows.

Other sections we would like included (not in any particular order):

-Why Choose KVT?:
Family-oriented team
Licensed & insured professionals
Residential & commercial expertise
Honest recommendations
Quality workmanship
Emergency service available
Clean, respectful technicians
One trusted company for plumbing and sewer solutions
____________________________
Our Story:
Built on solving complex plumbing challenges. Trusted for every plumbing need.
Since our founding, Conduit Renewal Partners has built a reputation for helping homeowners, businesses, and property managers solve some of the industry’s most challenging plumbing and sewer problems through quality workmanship, professionalism, and innovative solutions.
As our customers’ needs have grown, so has our commitment to serving them. What began as a leader in pipe restoration has expanded into full-service plumbing, allowing us to provide complete plumbing solutions—from everyday repairs and fixture replacements to water heaters, drain cleaning, repiping, and emergency plumbing services.
Today, our traditional plumbing division delivers the same level of expertise, communication, and customer care that KVT has become known for. Whether it’s a simple repair or a complex plumbing project, our goal remains the same: to provide dependable solutions, lasting quality, and an exceptional customer experience every step of the way.
-Our Values:
The KVT Way
Professional - Don't settle for good, BE GREAT
Responsive - When there's a need, BE FIRST!
Service - Life is not about you, BE ABOUT OTHERS!
These three values guide everything we do
Complete Plumbing Solutions:
-Plumbing Repairs
Reliable solutions to keep your plumbing system running safely and efficiently.
Leak detection & repair
Pipe Burst Repairs
Water line repairs
Whole-home repiping

-Fixtures & Installations
Professional installation, repair, and replacement of the fixtures you use every day.
Faucets
Toilets
Sinks
Showers & tubs
Garbage disposals
Hose bibs
Shut-off valves

-Water Heater Services
Whether you need a repair, replacement, or routine maintenance, we'll keep your hot water flowing.
Water heater repair
Water heater replacement
Tankless water heaters
Expansion tanks
Recirculation pumps
Preventative maintenance

-Drain & Sewer Solutions
From routine drain cleaning to complete sewer repairs, our team has the equipment and expertise to get your plumbing flowing again.
Drain cleaning
Hydro jetting
Camera inspections
Main sewer line cleaning
Sewer line repair
Sewer line replacement
Emergency drain backups
maybe add in a blurb saying
"Need a Trenchless Solution?
Ask about our non-invasive solutions as an alternative to traditional replacement for sewer and storm drain systems"
Testimonials:
"This company is fantastic, very professional and knowledgeable. Use them at several of my communities I manage and highly recommend them!" Belvine Townhomes
"KVT continues to be the primary plumbing vendor I use for all of my properties throughout Tampa Bay!" Corliss Dunes Condominium
"KVT did a great job at a great price and have always been willing to help with their abundance of knowledge prior to even working on projects for our community!" Townhomes at Hollow Fern
"KVT is amazing! My office flooded out on a Friday night and they responded within a couple hours to make the needed repair. The team was professional and got right to work (there van was also immaculate, which tells you a lot about hot they operate). Would definitely recommend them to anyone!" Dorin Welsby
______________________
Ready to get started?
Whether it's a leaking pipe, a new water heater, a clogged drain, or a plumbing emergency, our team is here to help
800-318-4957
info@kvtflow.example
www.kvtflow.example

Additional Information: please feel free to edit any of the pictures provided and AI files can be provided for the other marketing material if helpful. We would like an AI file and PDF ready print if possible.
Thank you!

commercial and residential property owners

Plumbing

Colors
0054AA
0677BA
7BADD7
CADEEF
E8F1F8

Must have
• My project must flow with current marketing material colors
Nice to have
• would like the front page picture to fade nicely into background

```html
<!DOCTYPE html>
<html lang="en">
<head>
<meta charset="utf-8">
<title>KVT Traditional Plumbing Trifold</title>
<link href="https://fonts.googleapis.com/css2?family=Rajdhani:wght@700&family=Roboto:wght@400;500&display=swap" rel="stylesheet">
<style>
:root{
  --navy:#1d2a7a;
  --brand:#0054AA;
  --ocean:#0677BA;
  --sky:#2a9fdc;
  --mist:#CADEEF;
  --ice:#f1f7fb;
  --ink:#1c1c1c;
  --stage:#ababab;
  --grad:linear-gradient(135deg,#2aa2dd 0%,#1f6ec0 50%,#1e2a7d 100%);
}
*{box-sizing:border-box;margin:0;padding:0}
html,body{width:771px;height:1200px;overflow:hidden;background:var(--stage)}
body{position:relative;font-family:'Roboto',sans-serif;color:var(--ink)}
.sheet{position:absolute;left:47.5px;width:675px;height:522px;box-shadow:0 6px 14px rgba(0,0,0,.25)}
.sheet--outside{top:56px;background:#fff}
.sheet--inside{top:620px;background:var(--ice)}
.panel{position:absolute;top:0;width:225px;height:100%}
.h-display{font-family:'Rajdhani',sans-serif;font-weight:700;text-transform:uppercase;line-height:1}
.photo{position:absolute;overflow:hidden}
.checklist{list-style:none}
.checklist li{position:relative;padding-left:17px}
.checklist li svg{position:absolute;left:0;top:1px;width:8px;height:8px}
/* outside */
.why{left:0}
.why h2{position:absolute;left:21px;top:19px;font-size:19.5px;color:#222}
.why .checklist{position:absolute;left:21px;top:50px;font-size:8px;font-weight:500;width:190px;color:#222}
.why .checklist li{margin-bottom:12.2px;line-height:12.3px}
.why .checklist li svg{top:2px}
.why .photo{left:0;top:264px;width:225px;height:258px;border-top-left-radius:30px;background:linear-gradient(160deg,#e9e8e3 0%,#bdb9b0 45%,#6e6b66 100%);border-top:4px solid var(--ocean)}
.cta{left:225px}
.cta .fill{position:absolute;left:0;top:0;width:225px;height:522px;background:var(--grad)}
.cta .photo{left:0;top:0;width:225px;height:264px;border-bottom-right-radius:30px;background:linear-gradient(150deg,#b97b5a 0%,#c9a58f 35%,#a5755e 60%,#2c2f3a 100%);border-right:3px solid var(--mist);border-bottom:3px solid var(--mist)}
.cta-body{position:absolute;left:0;top:290px;width:225px;color:#fff;text-align:center}
.cta-body h2{font-size:19px;line-height:23px}
.cta-body p{font-size:8px;font-weight:500;line-height:12.3px;margin-top:4px;padding:0 20px}
.contact{position:absolute;left:52px;display:flex;align-items:center;gap:8px;color:#fff;font-weight:500;font-size:10.5px}
.contact .dot{width:27px;height:27px;border-radius:50%;background:#fff;display:flex;align-items:center;justify-content:center}
.contact .dot svg{width:11px;height:11px}
.cover{left:450px}
.brand{position:absolute;left:0;width:225px;top:14px;text-align:center}
.brand .mark{display:inline-flex;align-items:center;gap:6px;font-family:'Rajdhani',sans-serif;font-weight:700;font-size:34px;line-height:1;color:var(--brand)}
.brand .mark i{display:block;width:22px;height:22px;background:var(--brand)}
.brand .sub{font-family:'Rajdhani',sans-serif;font-weight:700;font-size:6.5px;letter-spacing:1.4px;color:#222;margin-top:2px}
.title{position:absolute;left:0;width:225px;top:70px;text-align:center}
.title .t1{font-size:25px;color:#222}
.title .t2{font-size:35px;color:var(--brand);margin-top:2px;background:linear-gradient(90deg,#1e3f9c,#2b8fd6);-webkit-background-clip:text;background-clip:text;-webkit-text-fill-color:transparent}
.title .t3{font-size:25px;color:#222;margin-top:4px}
.cover .photo{left:0;top:172px;width:225px;height:150px;border-top-left-radius:30px;border-top:4px solid var(--ocean);background:linear-gradient(180deg,#c9b58f 0%,#d7d1c3 30%,#f2f2f2 55%,#9aa0a4 85%,#6a6a68 100%)}
.tagline{position:absolute;left:0;top:322px;width:225px;height:21px;background:var(--brand);color:#fff;font-family:'Rajdhani',sans-serif;font-weight:700;font-size:7.3px;letter-spacing:.2px;display:flex;align-items:center;justify-content:center}
.cover .checklist{position:absolute;left:32px;top:356px;font-size:12.5px;font-weight:500;color:#222}
.cover .checklist li{padding-left:20px;height:28.7px}
.cover .checklist li svg{width:11px;height:11px;top:2px}
.cover-contact{position:absolute;left:0;top:447px;width:225px;height:75px;background:var(--grad);color:#fff;font-weight:500;font-size:15px}
.cover-contact div{position:absolute;left:28px;display:flex;align-items:center;gap:12px}
.cover-contact svg{width:16px;height:16px}
/* inside */
.story{left:0;background:var(--ice);height:352px}
.story h2{position:absolute;left:21px;top:19px;font-size:19.5px;color:#222}
.story .copy{position:absolute;left:21px;top:44px;width:182px;font-size:8px;line-height:12.3px;text-align:justify;color:#222}
.story .copy p{margin-bottom:12.3px}
.complete{left:225px;height:352px;background:var(--grad);color:#fff}
.complete h2{position:absolute;left:21px;top:19px;font-size:19.5px;line-height:23px}
.complete h3{font-size:15px;line-height:17px;font-family:'Rajdhani',sans-serif;font-weight:700;text-transform:uppercase}
.group{position:absolute;left:22px;width:190px}
.group p{font-size:8px;line-height:12.3px;margin:4px 0 5px}
.group .checklist{font-size:8px;line-height:12.3px}
.group .checklist li{padding-left:15px}
.group .checklist li svg{top:2px}
.heaters{left:450px;height:352px;background:var(--ice)}
.heaters h2{font-size:19.5px;line-height:23px;color:#222}
.heaters .group{left:42px}
.heaters .checklist{color:#222;margin-top:3px}
.band{position:absolute;left:0;top:352px;width:675px;height:170px;background:linear-gradient(90deg,#3d4552 0%,#2d3440 40%,#3a4456 70%,#2a3140 100%)}
.trenchless{position:absolute;left:64.5px;top:57px;width:546px;height:65px;background:#fff;padding:3px}
.trenchless .inner{width:100%;height:100%;border:1.5px solid var(--navy);text-align:center;padding-top:9px}
.trenchless h2{font-size:19px;color:var(--navy)}
.trenchless p{font-size:8px;margin-top:8px;color:#222}
</style>
</head>
<body>
<svg width="0" height="0" style="position:absolute">
  <defs>
    <symbol id="tick" viewBox="0 0 16 16"><circle cx="8" cy="8" r="8" fill="currentColor"/><path d="M4.3 8.3l2.5 2.4 5-5" fill="none" stroke="#fff" stroke-width="2" stroke-linecap="round" stroke-linejoin="round"/></symbol>
  </defs>
</svg>

<section class="sheet sheet--outside">
  <div class="panel why">
    <h2 class="h-display">Why choose KVT?</h2>
    <ul class="checklist">
      <li><svg style="color:var(--sky)"><use href="#tick"/></svg>Family-oriented team</li>
      <li><svg style="color:var(--sky)"><use href="#tick"/></svg>Licensed &amp; insured professionals</li>
      <li><svg style="color:var(--sky)"><use href="#tick"/></svg>Residential &amp; commercial expertise</li>
      <li><svg style="color:var(--sky)"><use href="#tick"/></svg>Honest recommendations</li>
      <li><svg style="color:var(--sky)"><use href="#tick"/></svg>Quality workmanship</li>
      <li><svg style="color:var(--sky)"><use href="#tick"/></svg>Emergency service available</li>
      <li><svg style="color:var(--sky)"><use href="#tick"/></svg>Clean, respectful technicians</li>
      <li><svg style="color:var(--sky)"><use href="#tick"/></svg>One trusted company for plumbing<br>and sewer solutions</li>
    </ul>
    <div class="photo" role="img" aria-label="Technician working on pipes under a kitchen sink"></div>
  </div>

  <div class="panel cta">
    <div class="fill"></div>
    <div class="photo" role="img" aria-label="Hands wiring a tankless water heater on copper pipes"></div>
    <div class="cta-body">
      <h2 class="h-display">Ready to<br>get started?</h2>
      <p>Whether it's a leaking pipe, a new water heater, a clogged drain, or a plumbing emergency — our team is here to help.</p>
    </div>
    <div class="contact" style="top:386px"><span class="dot"><svg viewBox="0 0 24 24"><path d="M6.6 10.8a15 15 0 006.6 6.6l2.2-2.2a1 1 0 011-.25 11.4 11.4 0 003.6.57 1 1 0 011 1V20a1 1 0 01-1 1A17 17 0 013 4a1 1 0 011-1h3.5a1 1 0 011 1 11.4 11.4 0 00.57 3.6 1 1 0 01-.25 1z" fill="var(--brand)"/></svg></span>800-318-4957</div>
    <div class="contact" style="top:427px"><span class="dot"><svg viewBox="0 0 24 24"><rect x="2" y="5" width="20" height="14" rx="2" fill="var(--brand)"/><path d="M3 6l9 7 9-7" fill="none" stroke="#fff" stroke-width="1.6"/></svg></span>info@kvtflow.example</div>
    <div class="contact" style="top:468px"><span class="dot"><svg viewBox="0 0 24 24"><circle cx="12" cy="12" r="10" fill="var(--brand)"/><path d="M2 12h20M12 2c3 3 3 17 0 20M12 2c-3 3-3 17 0 20" fill="none" stroke="#fff" stroke-width="1.4"/></svg></span>www.kvtflow.example</div>
  </div>

  <div class="panel cover">
    <div class="brand">
      <div class="mark"><i></i>KVT</div>
      <div class="sub">CONDUIT RENEWAL PARTNERS</div>
    </div>
    <div class="title">
      <div class="h-display t1">Traditional</div>
      <div class="h-display t2">Plumbing</div>
      <div class="h-display t3">Services</div>
    </div>
    <div class="photo" role="img" aria-label="White branded service van parked in front of a building"></div>
    <div class="tagline">RELIABLE REPAIRS. HONEST SERVICE. LASTING SOLUTIONS.</div>
    <ul class="checklist">
      <li><svg style="color:var(--sky)"><use href="#tick"/></svg>Residential &amp; Commercial</li>
      <li><svg style="color:var(--sky)"><use href="#tick"/></svg>24/7 Emergency Service</li>
      <li><svg style="color:var(--sky)"><use href="#tick"/></svg>Licensed &amp; Insured</li>
    </ul>
    <div class="cover-contact">
      <div style="top:14px"><svg viewBox="0 0 24 24"><path d="M6.6 10.8a15 15 0 006.6 6.6l2.2-2.2a1 1 0 011-.25 11.4 11.4 0 003.6.57 1 1 0 011 1V20a1 1 0 01-1 1A17 17 0 013 4a1 1 0 011-1h3.5a1 1 0 011 1 11.4 11.4 0 00.57 3.6 1 1 0 01-.25 1z" fill="none" stroke="#fff" stroke-width="1.4"/></svg>800-318-4957</div>
      <div style="top:41px"><svg viewBox="0 0 24 24"><circle cx="12" cy="12" r="10" fill="none" stroke="#fff" stroke-width="1.4"/><path d="M2 12h20M12 2c3 3 3 17 0 20M12 2c-3 3-3 17 0 20" fill="none" stroke="#fff" stroke-width="1.4"/></svg>www.kvtflow.example</div>
    </div>
  </div>
</section>

<section class="sheet sheet--inside">
  <div class="panel story">
    <h2 class="h-display">Our story</h2>
    <div class="copy">
      <p>Built on solving complex plumbing challenges. Trusted for every plumbing need.</p>
      <p>Since our founding, Conduit Renewal Partners has built a reputation for helping homeowners, businesses, and property managers solve some of the industry's most challenging plumbing and sewer problems through quality workmanship, professionalism, and innovative solutions.</p>
      <p>As our customers' needs have grown, so has our commitment to serving them. What began as a leader in pipe restoration has expanded into full-service plumbing, allowing us to provide complete plumbing solutions—from everyday repairs and fixture replacements to water heaters, drain cleaning, repiping, and emergency plumbing services.</p>
      <p>Today, our traditional plumbing division delivers the same level of expertise, communication, and customer care that KVT has become known for.</p>
    </div>
  </div>

  <div class="panel complete">
    <h2 class="h-display">Complete plumbing<br>solutions</h2>
    <div class="group" style="top:77px">
      <h3>Plumbing repairs</h3>
      <p>Reliable solutions to keep your plumbing system running safely and efficiently.</p>
      <ul class="checklist">
        <li><svg style="color:#fff"><use href="#tick"/></svg>Leak detection &amp; repair</li>
        <li><svg style="color:#fff"><use href="#tick"/></svg>Pipe burst repairs</li>
        <li><svg style="color:#fff"><use href="#tick"/></svg>Water line repairs</li>
        <li><svg style="color:#fff"><use href="#tick"/></svg>Whole-home repiping</li>
      </ul>
    </div>
    <div class="group" style="top:195px">
      <h3>Fixtures &amp;<br>installations</h3>
      <p>Professional installation, repair, and replacement.</p>
      <ul class="checklist">
        <li><svg style="color:#fff"><use href="#tick"/></svg>Faucets</li>
        <li><svg style="color:#fff"><use href="#tick"/></svg>Toilets</li>
        <li><svg style="color:#fff"><use href="#tick"/></svg>Sinks</li>
        <li><svg style="color:#fff"><use href="#tick"/></svg>Showers &amp; tubs</li>
        <li><svg style="color:#fff"><use href="#tick"/></svg>Garbage disposals</li>
        <li><svg style="color:#fff"><use href="#tick"/></svg>Hose bibs</li>
        <li><svg style="color:#fff"><use href="#tick"/></svg>Shut-off valves</li>
      </ul>
    </div>
  </div>

  <div class="panel heaters">
    <div class="group" style="top:19px">
      <h2 class="h-display">Water heater<br>services</h2>
      <ul class="checklist">
        <li><svg style="color:var(--ocean)"><use href="#tick"/></svg>Water heater repair</li>
        <li><svg style="color:var(--ocean)"><use href="#tick"/></svg>Water heater replacement</li>
        <li><svg style="color:var(--ocean)"><use href="#tick"/></svg>Tankless water heaters</li>
        <li><svg style="color:var(--ocean)"><use href="#tick"/></svg>Expansion tanks</li>
        <li><svg style="color:var(--ocean)"><use href="#tick"/></svg>Recirculation pumps</li>
        <li><svg style="color:var(--ocean)"><use href="#tick"/></svg>Preventative maintenance</li>
      </ul>
    </div>
    <div class="group" style="top:154px">
      <h2 class="h-display">Drain &amp; sewer<br>solutions</h2>
      <ul class="checklist">
        <li><svg style="color:var(--ocean)"><use href="#tick"/></svg>Drain cleaning</li>
        <li><svg style="color:var(--ocean)"><use href="#tick"/></svg>Hydro jetting</li>
        <li><svg style="color:var(--ocean)"><use href="#tick"/></svg>Camera inspections</li>
        <li><svg style="color:var(--ocean)"><use href="#tick"/></svg>Main sewer line cleaning</li>
        <li><svg style="color:var(--ocean)"><use href="#tick"/></svg>Sewer line repair</li>
        <li><svg style="color:var(--ocean)"><use href="#tick"/></svg>Sewer line replacement</li>
        <li><svg style="color:var(--ocean)"><use href="#tick"/></svg>Emergency drain backups</li>
      </ul>
    </div>
  </div>

  <div class="band" role="img" aria-label="Dark photo of a hand fitting white PVC and brass pipe fittings">
    <div class="trenchless">
      <div class="inner">
        <h2 class="h-display">Need a trenchless solution?</h2>
        <p>Ask about our non-invasive solutions as an alternative to traditional replacement for sewer and storm drain systems.</p>
      </div>
    </div>
  </div>
</section>
</body>
</html>
```